Brantley Gutters 15"x12" EDDM flyer

Brantley Gutter a new seamless gutter company is looking for designs for an Every Door Direct Mailing (EDDM) piece. The dimensions will be 15" long and 12" high. Designs must be submitted with pms colors and be at least 300 dpi.

Brantley Gutters LLC.
The products you need at prices you can afford!!!

Brantley Gutters provides an excellent rain gutter system to protect your property. Our “factory on wheels” will custom fit seamless gutters to your home. Our goal is quality craftsmanship with top-notch service at a competitive price. We take pride in our installations, have excellent customer service and guarantee our products and services.

15% off new gutter installations
$50 off gutter repair
$139.00 gutter clean out special. May be additional fee if more than 100 lf. Single story homes only
$99 and up for gutter tune ups. Reseal all end caps and seems, reattach down spouts and align gutters/downspouts

Telephone number: 904-RAINPRO 904-724-7776 I would like the number on there both ways.

Website: brantleygutters-demo.com

We would like a neat, clean design (nothing to busy). I like the color palate of red, white, blue and black.

I have a preference of not having to buy images. Main reason is after going I'll provide my own images.

residential single family homes

neat and clean that states what we do

• Some play on the BG in Brantley Gutters but must be professional. A lot of our clients will call because their wives no longer want them getting up on ladder.

```html
<!DOCTYPE html>
<html lang="en">
<head>
<meta charset="utf-8">
<title>Brantley Gutters EDDM Mailer</title>
<link href="https://fonts.googleapis.com/css2?family=Open+Sans:wght@600;700&family=Source+Sans+3:wght@400;600;700&family=Arimo:wght@400;700&display=swap" rel="stylesheet">
<style>
  :root{
    --blue:#1565b8;
    --blue-dark:#123f85;
    --blue-text:#1a6cc4;
    --grey-tab:#a7a9ac;
    --panel:#e9ecef;
    --ink:#222;
    --page:#e4e4e4;
    --white:#fff;
  }
  *{box-sizing:border-box;margin:0;padding:0}
  html,body{width:855px;height:1200px;overflow:hidden;background:var(--page)}
  body{position:relative;font-family:"Source Sans 3",sans-serif;color:var(--ink)}
  .card{position:absolute;width:648px;height:517px;background:var(--white);overflow:hidden}
  .card--front{left:53px;top:46px}
  .card--back{left:117px;top:598px}

  .photo{position:absolute}
  .front-photo{left:0;top:0;width:401px;height:463px;
    background:linear-gradient(180deg,#dcecf7 0%,#b9d3e6 22%,#8a6a52 48%,#a0714d 70%,#6d4a33 100%)}
  .front-headline{position:absolute;left:0;top:27px;width:401px;text-align:center;
    font-family:"Open Sans",sans-serif;font-weight:700;font-size:18.5px;line-height:24px;color:var(--blue-text)}

  .offers{position:absolute;left:401px;top:0;width:247px;height:463px;background:var(--panel)}
  .offer{position:absolute;left:4px;width:238px;height:107px;background:#f7f8f9;border:1px dashed #8aa6c8}
  .offer-bar{position:absolute;left:0;top:0;width:100%;height:24px;background:var(--blue);
    color:var(--white);font-weight:700;font-size:11.5px;line-height:24px;padding-left:64px;white-space:nowrap}
  .offer-price{position:absolute;left:0;top:0;width:60px;height:46px;background:var(--blue);
    border-radius:0 0 30px 30px;color:var(--white);font-family:"Source Sans 3",sans-serif;
    font-weight:600;font-size:25px;line-height:40px;text-align:center;letter-spacing:-1px}
  .offer-price small{font-size:14px;letter-spacing:0}
  .offer-photo{position:absolute;right:0;top:24px;width:115px;height:82px;
    background:linear-gradient(90deg,rgba(247,248,249,1) 0%,rgba(210,214,218,.9) 45%,#9fa6ad 100%)}
  .offer-note{position:absolute;left:30px;top:58px;width:180px;text-align:center;font-size:8px;line-height:11px;color:#222}

  .name-tab{position:absolute;left:0;top:446px;width:300px;height:48px;background:var(--grey-tab);
    clip-path:polygon(0 0,100% 0,84% 100%,0 100%);z-index:2}
  .name-tab span{position:absolute;left:19px;top:6px;font-family:"Open Sans",sans-serif;font-weight:600;font-size:28px;color:var(--white);white-space:nowrap}
  .phone-band{position:absolute;left:0;top:463px;width:648px;height:54px;
    background:linear-gradient(90deg,var(--blue) 0%,var(--blue-dark) 100%)}
  .phone-line{position:absolute;right:14px;top:13px;display:flex;align-items:center;gap:6px;
    font-family:"Open Sans",sans-serif;font-weight:700;font-size:23px;color:var(--white);white-space:nowrap;z-index:3}
  .phone-line svg{width:22px;height:22px}

  .back-photo{left:0;top:0;width:430px;height:211px;
    background:linear-gradient(180deg,#cfe0c8 0%,#9bb88a 35%,#8d6a4f 55%,#b08461 75%,#4f7a3a 100%)}
  .back-headline{position:absolute;left:0;top:211px;width:430px;height:70px;background:var(--blue);
    color:var(--white);text-align:center;font-family:"Open Sans",sans-serif;font-weight:700;font-size:18.5px;line-height:25px;padding-top:11px}
  .back-copy{position:absolute;left:0;top:281px;width:430px;height:182px;background:#f2f2f2;padding:14px 16px 0 24px}
  .back-copy p{font-size:11.8px;line-height:15.2px;text-align:justify;margin-bottom:15px}
  .brand{color:var(--blue-text)}
  .site-tab{position:absolute;left:0;top:428px;width:350px;height:50px;background:var(--grey-tab);
    clip-path:polygon(0 0,100% 0,86% 100%,0 100%);z-index:2}
  .site-tab span{position:absolute;left:24px;top:10px;font-family:"Open Sans",sans-serif;font-weight:700;font-size:19px;line-height:26px;color:var(--white);white-space:nowrap}
  .back-band{top:463px;z-index:1}
  .back-band .phone-line{z-index:3}
  .back-band{overflow:visible}
  .return-address{position:absolute;left:445px;top:33px;font-size:12.5px;line-height:15.5px;font-style:normal}
  .return-address .brand{display:block}
  .indicia{position:absolute;left:581px;top:20px;width:55px;height:53px;border:1px solid #555;
    font-family:"Arimo",sans-serif;font-size:7.3px;line-height:8.6px;text-align:center;padding-top:3px}
  .indicia b{font-weight:700}
  .mail-block{position:absolute;left:450px;top:151px;width:185px;height:74px;border:1px solid #999;font-family:"Arimo",sans-serif}
  .mail-block .route{position:absolute;right:14px;top:11px;font-size:8px;letter-spacing:.2px}
  .mail-block .recipient{position:absolute;left:14px;top:36px;font-size:11px;line-height:13px}
</style>
</head>
<body>
  <section class="card card--front">
    <div class="photo front-photo" role="img" aria-label="Photo of a house eave with copper gutters, cedar shingle siding and a white window"></div>
    <h1 class="front-headline">THE PRODUCTS YOU NEED<br>AT PRICES YOU CAN AFFORD!!!</h1>

    <div class="offers">
      <div class="offer" style="top:13px">
        <div class="offer-photo" role="img" aria-label="Photo of a new seamless gutter and downspout"></div>
        <div class="offer-bar">NEW GUTTER INSTALLATIONS</div>
        <div class="offer-price">15<small>% off</small></div>
        <p class="offer-note">We will come out and custom build<br>seamless gutters to form your home.</p>
      </div>
      <div class="offer" style="top:124px">
        <div class="offer-photo" role="img" aria-label="Photo of a hand repairing a gutter"></div>
        <div class="offer-bar">GUTTER REPAIR</div>
        <div class="offer-price">50 <small>$</small></div>
        <p class="offer-note">Customer should know<br>if they need a repair</p>
      </div>
      <div class="offer" style="top:235px">
        <div class="offer-photo" role="img" aria-label="Photo of a gutter full of leaves"></div>
        <div class="offer-bar">GUTTER CLEAN OUT SPECIAL</div>
        <div class="offer-price">139 <small>$</small></div>
        <p class="offer-note">May be additional fee if more than 100 lf<br>Single story homes only</p>
      </div>
      <div class="offer" style="top:346px">
        <div class="offer-photo" role="img" aria-label="Photo of a gutter along a roof edge"></div>
        <div class="offer-bar" style="padding-left:60px">AND UP FOR GUTTER TUNE UPS</div>
        <div class="offer-price">99 <small>$</small></div>
        <p class="offer-note">Reseal all end caps and seems,<br>reattach down spouts and align gutters</p>
      </div>
    </div>

    <div class="name-tab"><span>Brantley Gutter</span></div>
    <div class="phone-band">
      <div class="phone-line">
        <svg viewBox="0 0 24 24" aria-hidden="true"><circle cx="12" cy="12" r="10.5" fill="none" stroke="#fff" stroke-width="1.8"/><path d="M8.6 6.8l1.8-.4 1.2 2.8-1.3 1a6.5 6.5 0 0 0 3.5 3.5l1-1.3 2.8 1.2-.4 1.8c-.2.6-.8 1-1.4.9A9 9 0 0 1 7.7 8.2c-.1-.6.3-1.2.9-1.4z" fill="#fff"/></svg>
        <span>904-RAINPRO&nbsp; 904-724-7776</span>
      </div>
    </div>
  </section>

  <section class="card card--back">
    <div class="photo back-photo" role="img" aria-label="Photo of a shingle-sided home with a white columned porch and landscaping"></div>
    <h2 class="back-headline">THE PRODUCTS YOU NEED<br>AT PRICES YOU CAN AFFORD!!!</h2>
    <div class="back-copy">
      <p><span class="brand">Brantley Gutters</span> provides an excellent rain gutter system to protect your property. Our “factory on wheels” will custom fit seamless gutters to your home. Our goal is quality craftsmanship with top-notch service at a competitive price. We take pride in our installations, have excellent customer service and guarantee our products and services.</p>
      <p>Brantley Gutters installs, repairs, cleans and performs tune ups to seamless gutters. We only install 6" K style gutters.</p>
    </div>

    <address class="return-address">
      <span class="brand">Brantley Gutters LLC.</span>
      418 Harbor View Rd<br>Fernlake, NY 14092
    </address>
    <div class="indicia">PRSRT STD<br>ECRWSS<br>U.S. Postage<br><b>PAID</b><br>EDDM RETAIL</div>
    <div class="mail-block">
      <span class="route">****************ECRWSS****</span>
      <span class="recipient">Local<br>Postal Customer</span>
    </div>

    <div class="phone-band back-band">
      <div class="phone-line">
        <svg viewBox="0 0 24 24" aria-hidden="true"><circle cx="12" cy="12" r="10.5" fill="none" stroke="#fff" stroke-width="1.8"/><path d="M8.6 6.8l1.8-.4 1.2 2.8-1.3 1a6.5 6.5 0 0 0 3.5 3.5l1-1.3 2.8 1.2-.4 1.8c-.2.6-.8 1-1.4.9A9 9 0 0 1 7.7 8.2c-.1-.6.3-1.2.9-1.4z" fill="#fff"/></svg>
        <span>904-RAINPRO&nbsp; 904-724-7776</span>
      </div>
    </div>
    <div class="site-tab"><span>brantleygutters-demo.com</span></div>
  </section>
</body>
</html>
```